I need a business card design for my new clinic (SPORTS MEDICINE OF KNEE). I am orthopedist, expert in sports surgery, especially knee surgery. I prefer, as colors, the colors of my logo (green, black and white). I already have my logo and should appear on my card. It's good to see my site to have ideas (www.drlucianovarela.com)
It needs contain:
my name: Dr. Luciano Varela
my registration: CRM 584-902
my specialty: Cirurgia do Joelho / Esporte
my address: Centro Executivo - Pinheiral Plaza
Av. Doutor Augusto Brandão Cunha, 2740 sala 0836
Jd. Ipanema - Ribeirão Preto - SP
my phone number: Tel (16) 8245-3908
my clinic phone: (16) 3670-4851
my e-mail: drlucianovarela@mailbox-exemplo.com
my site: www.drlucianovarela.com

Target Market(s)

futures patients

Industry/Entity Type

Clinic

Requirements
Nice to have
• letters not overfilled
straight lines, with few curves

```html
<!DOCTYPE html>
<html lang="pt-BR">
<head>
<meta charset="utf-8">
<title>Dr. Luciano Varela — Cartão de Visita</title>
<link rel="stylesheet" href="https://fonts.googleapis.com/css2?family=Source+Sans+3:wght@400&display=swap">
<style>
  :root {
    --ink: #111111;
    --card: #ffffff;
    --green: #86bf8c;
    --rule: #555555;
    --text-dark: #1a1a1a;
    --text-light: #ffffff;
    --font: "Source Sans 3", sans-serif;
  }
  * { margin: 0; padding: 0; box-sizing: border-box; }
  html, body { width: 693px; height: 1200px; overflow: hidden; background: var(--card); }
  .card {
    position: relative;
    width: 693px;
    height: 1200px;
    background: var(--card);
    font-family: var(--font);
    color: var(--text-dark);
    overflow: hidden;
  }
  .brand {
    position: absolute;
    left: 113px;
    top: 96px;
    display: flex;
    align-items: center;
    gap: 26px;
  }
  .brand-mark {
    width: 115px;
    height: 109px;
    background: var(--ink);
    border-radius: 10px;
  }
  .brand-name {
    font-size: 88px;
    line-height: 1;
    letter-spacing: 4px;
    color: var(--ink);
  }
  .centered {
    position: absolute;
    left: 0;
    width: 100%;
    text-align: center;
    white-space: nowrap;
  }
  .doctor-name { top: 272px; font-size: 37px; line-height: 48px; letter-spacing: 0.3px; }
  .registration { top: 337px; font-size: 21px; line-height: 28px; }
  .divider {
    position: absolute;
    left: 77px;
    top: 402px;
    width: 534px;
    height: 2px;
    background: var(--rule);
  }
  .specialty { top: 465px; font-size: 37px; line-height: 48px; letter-spacing: 0.3px; }
  .phone { font-size: 40px; line-height: 50px; letter-spacing: 0.3px; }
  .phone-mobile { top: 554px; }
  .phone-clinic { top: 599px; }
  .band-transition {
    position: absolute;
    left: 0;
    top: 715px;
    width: 693px;
    height: 245px;
    background: linear-gradient(180deg, var(--card) 0%, var(--green) 30%, var(--ink) 100%);
  }
  .band-base {
    position: absolute;
    left: 0;
    top: 960px;
    width: 693px;
    height: 240px;
    background: var(--ink);
  }
  .contact-block { color: var(--text-light); }
  .address { font-size: 27px; line-height: 34px; top: 979px; letter-spacing: 0.4px; }
  .online { font-size: 26px; line-height: 33px; top: 1106px; letter-spacing: 0.3px; }
</style>
</head>
<body>
<main class="card">
  <div class="band-transition" role="img" aria-label="Decorative green and white wave leading into the black contact band"></div>
  <div class="band-base"></div>

  <header class="brand">
    <div class="brand-mark"></div>
    <span class="brand-name">VARELA</span>
  </header>

  <p class="centered doctor-name">Dr. Luciano Varela</p>
  <p class="centered registration">CRM 584-902</p>
  <div class="divider"></div>

  <p class="centered specialty">Specialty: Cirurgia do Joelho / Esporte</p>
  <p class="centered phone phone-mobile">Tel: (16) 8245-3908</p>
  <p class="centered phone phone-clinic">Clinic phone: (16) 3670-4851</p>

  <section class="contact-block">
    <p class="centered address">Centro Executivo - Pinheiral Plaza<br>Av. Doutor Augusto Brandão Cunha, 2740 sala 0836<br>Jd. Ipanema - Ribeirão Preto - SP</p>
    <p class="centered online">e-mail: drlucianovarela@mailbox-exemplo.com<br>www.drlucianovarela.com</p>
  </section>
</main>
</body>
</html>
```